Professional Personal Wordpress Blog Theme

I need a RESPONSIVE design for my personal website at DarrowPlaskett.com that focuses on me as an entrepreneur (CrowdPulse.com, BoutLinker.com, and then the ability to talk about others). My focus on combative sports maybe some still images from this youtube http://vidsharo.example/q7Lm2Xp (possibly in a boxing/muay thai) ring or cage) or a video overlay like on CrowdPulse.com. I very much like the style of CrowdPulse.com but want a real custom feel to my personal blog. MUST INCLUDE views on multiple devices to get the project (desktop, tablet, and smart phone). Think cutting edge/Bleeding edge design for 2015 that focuses on lots of great blog content. No separate categories needed just a really modern homepage and awesome blog layout that has a pro feel while at the same time Brimstoke like (but no skulls and cross bone stuff). If you want to use a background video like on CrowdPulse.com that could work as well. This is a COMPLETE design and theme creation. I need a theme that I can just drop the theme into wordpress if you cannot do the design and then create the theme please do not submit anything.
Updates

Note this is for a full Wordpress theme not just the design. Please do not submit if you aren't also providing a full wordpress theme. Thank you!

Think boxing, kickboxing, muay thai, jiu jitsu, etc.

If you are working on this project or have any questions please let me know. I'm trying to determine if anyone is actively using SketchHive.com because I haven't received any questions or feedback yet. Thanks for taking a look & I hope to find someone to work with soon!

Please check out the files I uploaded to get an idea of what I am looking for. It can deviate but should be something like that if possible (of course it needs to be responsive so some modifications for screen sizes should be made).

In addition to the layout provided in the zip file it would also be good to provide a search bar in the top left of the header (every page) for searching the blog. In addition, easy ways to navigate the site including possibly a nicely designed sitepmap page and related posts on the blog article/single page.

In addition to what I provided (the layouts) I'm also thinking I'd like to see a search layout in the top left of the header and then more creative ways for the site to be navigated (more links) plus, possibly a designed sitemap. Finally, for the responsive portion of the single/blog article page I would want the content of the article to show right below the header and then the sidebar shifted below the article but before the footer.

Target Market(s)

My readers are typically on mobile devices (tablets & smart phones) and in general are other entrepreneurs or martial artists. Fonts should be modern and interesting (not just basic, boring fonts).

Think Rex Dunmore, Hank Bordell, rugged, tough, fighters

Industry/Entity Type

Entrepreneur

Requirements
Must have
• Must be responsive and look great on all devices (desktops, tablets, smart phones). I need a full custom theme that can be dropped right into wordpress. So you must code the theme as well as prepare the design.

Feel free to use pixvault images as I have an account with them.
Nice to have
• Cool modern looking fonts I like the following font (the blog post title here): http://devnotes.quorvix.example/featured/crowdpulse-social-app-sports-enthusiasts-built-quorvix-platform/

The main feature of the site should be blog articles. No need for anything else no poems, videos, etc. Just an awesome blog layout.

The colors should be strong colors Red, Black, Blue, Green, Orange
Should not have
• No cartoons, no unlicensed images (use pixvault please and note the images for me to download in final form). No script looking fonts.

The attached file are just ideas but the flow and concepts should be pretty clear. Please ask if you have any questions.

```html
<!DOCTYPE html>
<html lang="en">
<head>
<meta charset="utf-8">
<title>Darrow Plaskett</title>
<link rel="stylesheet" href="https://fonts.googleapis.com/css2?family=Roboto+Slab:wght@400;700&family=Roboto+Condensed:wght@300;400;700&family=Open+Sans:wght@400;600&display=swap">
<style>
:root{
  --red:#e8232a;
  --red-deep:#b51317;
  --orange:#f26a0c;
  --black:#0b0b0b;
  --charcoal:#1c1c1c;
  --green:#3cf01f;
  --button:#4cb81a;
  --cream:#fdfbe8;
  --white:#ffffff;
  --muted:#9a9a8e;
}
*{margin:0;padding:0;box-sizing:border-box}
html,body{width:1200px;height:2350px;overflow:hidden;background:var(--black)}
body{position:relative;font-family:"Open Sans",sans-serif;color:var(--white)}

/* Header + hero */
.hero{position:absolute;left:0;top:0;width:1200px;height:675px;
  background:radial-gradient(ellipse at 50% 30%,#3a3a3a 0%,#161616 45%,#050505 100%)}
.hero-photo{position:absolute;left:150px;top:330px;width:900px;height:345px;
  background:radial-gradient(ellipse at 30% 55%,rgba(170,20,30,.75) 0%,rgba(90,10,15,.4) 30%,transparent 60%),
             radial-gradient(ellipse at 72% 55%,rgba(170,20,30,.75) 0%,rgba(90,10,15,.4) 30%,transparent 60%)}
.topbar{position:absolute;left:0;top:0;width:1200px;height:89px;
  border-bottom:2px solid rgba(232,35,42,.55);box-shadow:0 4px 14px rgba(232,35,42,.25)}
.site-title{position:absolute;left:0;top:20px;width:1200px;text-align:center;
  font-family:"Roboto Slab",serif;font-weight:700;font-size:43px;color:var(--red);letter-spacing:1px}
.nav{position:absolute;left:107px;top:119px;display:flex;gap:26px;list-style:none}
.nav li{font-family:"Roboto Condensed",sans-serif;font-size:13px;font-weight:700;
  height:28px;line-height:28px;color:var(--white)}
.nav li.active{background:var(--red);border-radius:14px;padding:0 20px}
.search{position:absolute;left:840px;top:114px;width:255px;height:37px;border-radius:19px;
  border:1px solid #3a3a3a;background:#0c0c0c;font-size:11px;color:#777;padding:11px 20px}
.tagline{position:absolute;left:0;top:200px;width:1200px;text-align:center;
  font-family:"Roboto Slab",serif;font-weight:400;line-height:1}
.tagline span{display:block;margin-bottom:8px}
.tagline .l1{color:var(--green);font-size:62px}
.tagline .l2{color:var(--red);font-size:52px}
.tagline .l3{color:var(--white);font-size:52px}

/* Section headings */
.section-head{position:absolute;left:298px;width:590px;height:78px;text-align:center}
.section-head .frame{position:absolute;left:0;top:18px;width:590px;height:58px;
  border:2px solid var(--white);border-top:none}
.section-head .frame::before,.section-head .frame::after{content:"";position:absolute;top:0;height:2px;background:var(--white);width:60px}
.section-head .frame::before{left:0}
.section-head .frame::after{right:0}
.section-head h2{position:relative;font-family:"Roboto Condensed",sans-serif;font-weight:700;font-size:37px;line-height:36px;color:var(--white)}
.section-head p{position:relative;margin-top:12px;font-family:"Roboto Condensed",sans-serif;font-weight:300;font-size:36px;line-height:36px;color:var(--white)}
.section-head p b{font-weight:300;padding:0 14px}
.section-head .frame-bottom-gap{position:absolute;left:0;top:52px;width:590px}

/* Companies */
.companies{position:absolute;left:0;top:675px;width:1200px;height:518px;
  background:radial-gradient(ellipse at 50% 40%,#c9191d 0%,var(--red-deep) 60%,#9a0f12 100%)}
.logo-strip{position:absolute;left:92px;width:1003px;background:var(--white);
  display:flex;align-items:center;justify-content:space-around;padding:0 8px;border:3px solid var(--white)}
.strip-1{top:172px;height:90px}
.strip-2{top:276px;height:95px}
.strip-3{top:383px;height:91px}
.brand{display:flex;align-items:center;gap:8px;height:72px;padding:0 14px;
  font-family:"Roboto Condensed",sans-serif;font-weight:700;font-size:30px;color:#1a1a1a;white-space:nowrap}
.brand i{display:block;width:20px;height:20px;border-radius:50%;background:currentColor}
.brand.dark{background:#1a1010;color:var(--white)}
.brand.blue{color:#1d5fa6}
.brand.grey{color:#3f6d8c}
.brand.pink{color:#d8336b}
.brand.orange{color:#e8532a}
.brand.more{background:#180b0b;color:#2b8de2;font-size:28px;line-height:26px;text-align:center;width:140px;justify-content:center;border-radius:4px}

/* Articles */
.articles-top{position:absolute;left:0;top:1193px;width:1200px;height:307px;background:var(--orange)}
.articles-bottom{position:absolute;left:0;top:1500px;width:1200px;height:745px;background:#151515}
.cards{position:absolute;left:105px;top:1324px;width:978px;display:grid;
  grid-template-columns:repeat(4,233px);column-gap:15px;row-gap:23px}
.card{height:424px;background:var(--cream);padding:7px;text-align:center;box-shadow:0 2px 8px rgba(0,0,0,.35)}
.card .photo{height:164px}
.card h3{margin-top:32px;font-family:"Roboto Condensed",sans-serif;font-weight:400;font-size:20px;color:#ec3b16;text-transform:uppercase}
.card h4{margin-top:10px;font-family:"Roboto Condensed",sans-serif;font-weight:400;font-size:20px;color:#151515;text-transform:uppercase}
.card hr{width:110px;margin:22px auto 18px;border:none;border-top:1px solid #d8d6c4}
.card p{font-size:10.5px;line-height:16px;color:var(--muted);text-transform:uppercase;padding:0 24px}
.card .btn{display:inline-block;margin-top:22px;width:115px;height:36px;line-height:36px;
  background:var(--button);color:var(--white);font-family:"Roboto Condensed",sans-serif;font-size:12px;border-radius:2px}
.p1{background:linear-gradient(160deg,#2a3ccf,#7a2a8a 55%,#121530)}
.p2{background:linear-gradient(180deg,#3a2418,#8a5a3a 50%,#2a1810)}
.p3{background:linear-gradient(180deg,#1a1a1a,#6a4030 55%,#2a1a14)}
.p4{background:linear-gradient(180deg,#5a6a7a,#3a3a3a 60%,#1a1a1a)}
.p5{background:linear-gradient(180deg,#2a2a2a,#4a4040 55%,#141414)}
.p6{background:linear-gradient(180deg,#4a5050,#7a5a48 55%,#2a2a2a)}
.p7{background:linear-gradient(180deg,#1a1a1a,#8a8a8a 50%,#2a2a2a)}
.p8{background:linear-gradient(180deg,#3a3a3a,#6a5040 55%,#2a1f18)}

/* Footer */
.footer{position:absolute;left:0;top:2245px;width:1200px;height:105px;
  background:linear-gradient(180deg,#0c0c0c,#050505);border-top:1px solid #222;text-align:center}
.footer p{margin-top:24px;font-size:11px;color:#8a8a8a;text-transform:uppercase}
.footer::after{content:"";position:absolute;left:0;bottom:0;width:1200px;height:3px;background:linear-gradient(90deg,transparent,var(--red-deep),transparent)}
</style>
</head>
<body>

<header class="hero">
  <div class="hero-photo" role="img" aria-label="Pair of red boxing gloves facing each other on a dark background"></div>
  <div class="topbar"><h1 class="site-title">DARROW PLASKETT</h1></div>
  <ul class="nav">
    <li class="active">HOME</li>
    <li>BLOG</li>
    <li>CONTACT ME</li>
  </ul>
  <div class="search">Search here</div>
  <div class="tagline">
    <span class="l1">FIGHT THE GOOD FIGHT</span>
    <span class="l2">AND FORGIVE OR FORGET</span>
    <span class="l3">THE REST</span>
  </div>
</header>

<section class="companies" role="img" aria-label="Red-toned backdrop of two fighters facing off">
  <div class="section-head" style="top:40px">
    <div class="frame"></div>
    <h2>COMPANIES POWERED BY</h2>
    <p><b style="background:var(--red-deep)">DARROW PLASKETT</b></p>
  </div>
  <div class="logo-strip strip-1">
    <div class="brand dark"><i></i>BoutLinker</div>
    <div class="brand dark">CrowdPulse</div>
    <div class="brand dark"><i></i>GrappleFed</div>
    <div class="brand grey" style="background:#f2f2f2">HomeTendr.com</div>
  </div>
  <div class="logo-strip strip-2">
    <div class="brand" style="font-size:40px"><i style="width:14px;height:14px;color:var(--red)"></i>StudyPath</div>
    <div class="brand">Ridgeback Leads</div>
    <div class="brand blue"><i></i>PorchLine</div>
    <div class="brand blue" style="background:#e4eef8">DegreeHarbor.com</div>
  </div>
  <div class="logo-strip strip-3">
    <div class="brand grey" style="font-size:22px">Elmbrook Nannies</div>
    <div class="brand orange"><i></i>KVX</div>
    <div class="brand pink">SitterGuild.com</div>
    <div class="brand grey">CarerNest</div>
    <div class="brand more">MANY<br>MORE</div>
  </div>
</section>

<div class="articles-top"></div>
<div class="articles-bottom"></div>
<div class="section-head" style="top:1212px">
  <div class="frame"></div>
  <h2>ARTICLES &amp; MORE BY</h2>
  <p><b style="background:var(--orange)">DARROW PLASKETT</b></p>
</div>

<main class="cards">
  <article class="card"><div class="photo p1" role="img" aria-label="Empty boxing ring under blue and purple lights"></div><h3>Lorem ipsum dolor</h3><h4>Sit amet</h4><hr><p>Ut wisi enim ad minim veniam, quis nostrud exerci tation ullamcorper susciese molestie.</p><span class="btn">DEATILS</span></article>
  <article class="card"><div class="photo p2" role="img" aria-label="Boxer bending forward in a corner"></div><h3>Bubo valencia</h3><h4>Esta di maria</h4><hr><p>Ut wisi enim ad minim veniam, quis nostrud exerci tation ullamcorper susciese molestie.</p><span class="btn">DEATILS</span></article>
  <article class="card"><div class="photo p3" role="img" aria-label="Boxer in red gloves in a guard stance"></div><h3>Praesebus nat oqu</h3><h4>Et gnis dent mo</h4><hr><p>Ut wisi enim ad minim veniam, quis nostrud exerci tation ullamcorper susciese molestie.</p><span class="btn">DEATILS</span></article>
  <article class="card"><div class="photo p4" role="img" aria-label="Referee raising the winner's arm in a ring"></div><h3>Duice feug uada</h3><h4>Ne feugiat mada</h4><hr><p>Ut wisi enim ad minim veniam, quis nostrud exerci tation ullamcorper susciese molestie.</p><span class="btn">DEATILS</span></article>
  <article class="card"><div class="photo p5" role="img" aria-label="Tired boxer resting on the ring ropes"></div><h3>Fusce susci</h3><h4>Uscipit variusciis</h4><hr><p>Ut wisi enim ad minim veniam, quis nostrud exerci tation ullamcorper susciese molestie.</p><span class="btn">DEATILS</span></article>
  <article class="card"><div class="photo p6" role="img" aria-label="Two fighters exchanging punches in a cage"></div><h3>Morbnavida at,</h3><h4>Odiof, gravida</h4><hr><p>Ut wisi enim ad minim veniam, quis nostrud exerci tation ullamcorper susciese molestie.</p><span class="btn">DEATILS</span></article>
  <article class="card"><div class="photo p7" role="img" aria-label="Fighter striking a heavy bag in a cloud of chalk"></div><h3>Nul feugiatuada</h3><h4>Feugiat malesuada</h4><hr><p>Ut wisi enim ad minim veniam, quis nostrud exerci tation ullamcorper susciese molestie.</p><span class="btn">DEATILS</span></article>
  <article class="card"><div class="photo p8" role="img" aria-label="Kickboxer throwing a high kick in a gym"></div><h3>Viviuos set ests mes</h3><h4>Enno ruthless</h4><hr><p>Ut wisi enim ad minim veniam, quis nostrud exerci tation ullamcorper susciese molestie.</p><span class="btn">DEATILS</span></article>
</main>

<footer class="footer"><p>© 2015 DarrowPlaskett.com all rights reserved.</p></footer>

</body>
</html>
```